Flyer, Anzeige & Aufkleber für Massagen gestalten
Zielgruppe
Massage. Gaymassage. Wellness. Kosmetik
Aufgabenstellung
Anfertigung eines Flyers, Anzeige und Aufkleber ....

```html
<!DOCTYPE html>
<html lang="de">
<head>
<meta charset="utf-8">
<title>Velorin Point – Flyer</title>
<link rel="stylesheet" href="https://fonts.googleapis.com/css2?family=Open+Sans:wght@400&family=PT+Sans:wght@700&family=Signika:wght@600&display=swap">
<style>
  :root {
    --ink: #ffffff;
    --night: #05040c;
    --deep-blue: #1a1850;
    --glow-blue: #3c3fa0;
    --lilac: #a57aa8;
    --plum: #6d3f72;
    --tag-ink: #1b1420;
    --paper: #e6e6e6;
  }
  * { margin: 0; padding: 0; box-sizing: border-box; }
  html, body { width: 1200px; height: 872px; overflow: hidden; background: var(--night); }
  .flyer { position: relative; width: 1200px; height: 872px; overflow: hidden; color: var(--ink); }
  .backdrop {
    position: absolute; inset: 0;
    background:
      radial-gradient(ellipse 70% 45% at 45% 58%, var(--glow-blue) 0%, var(--deep-blue) 45%, transparent 80%),
      linear-gradient(180deg, #111018 0%, #0a0a1a 40%, #0c0c26 75%, #141320 100%);
  }
  .services-line {
    position: absolute; left: 185px; top: 26px;
    font: 700 37px/1 "PT Sans", sans-serif; letter-spacing: -0.5px;
  }
  .brand-name { position: absolute; left: 50px; top: 60px; width: 960px; height: 110px; }
  .brand-name text { font-family: "PT Sans", sans-serif; font-weight: 700; font-size: 128px; fill: var(--ink); }
  .phone {
    position: absolute; left: 152px; top: 252px;
    font: 700 64px/1 "PT Sans", sans-serif; letter-spacing: -2px;
  }
  .offer-tag { position: absolute; left: 20px; top: 332px; width: 210px; height: 310px; }
  .offer-tag text { font-family: "Signika", sans-serif; fill: var(--tag-ink); }
  .treatments { position: absolute; inset: 0; list-style: none; font: 600 60px/1 "Signika", sans-serif; }
  .treatments li { position: absolute; white-space: nowrap; }
  .treatments li::before { content: "•"; margin-right: 24px; }
  .photo { position: absolute; }
  .address {
    position: absolute; left: 320px; top: 718px;
    font: 700 38px/1 "PT Sans", sans-serif; letter-spacing: -0.5px; white-space: nowrap;
  }
  .website {
    position: absolute; left: 204px; top: 760px;
    font: 400 82px/1 "Open Sans", sans-serif; letter-spacing: -1px;
  }
</style>
</head>
<body>
<div class="flyer">
  <div class="backdrop" role="img" aria-label="Dunkler Hintergrund mit leuchtendem blauem Lichtnetz"></div>

  <div class="services-line">Haus Hotel Outdoor</div>

  <svg class="brand-name" viewBox="0 0 960 110">
    <text x="0" y="98" textLength="700" lengthAdjust="spacingAndGlyphs">Velorin Point</text>
  </svg>

  <div class="phone">Tel. 0160 - 482 93 17</div>

  <svg class="offer-tag" viewBox="0 0 210 310">
    <g transform="rotate(-14 105 155)">
      <rect x="40" y="20" width="140" height="280" rx="6" fill="var(--plum)"/>
      <rect x="30" y="15" width="140" height="280" rx="6" fill="var(--lilac)"/>
      <rect x="22" y="5" width="80" height="38" rx="4" fill="var(--paper)"/>
      <polygon points="170,295 170,245 115,295" fill="#d6d6d6"/>
      <text x="100" y="85" font-size="27" text-anchor="middle">Open</text>
      <text x="100" y="112" font-size="27" text-anchor="middle">daily</text>
      <text x="100" y="178" font-size="38" text-anchor="middle">56 €/</text>
      <text x="100" y="210" font-size="22" text-anchor="middle">Stunde</text>
    </g>
  </svg>

  <ul class="treatments">
    <li style="left:318px;top:382px">Ganzkörper</li>
    <li style="left:297px;top:452px">Po-Relax</li>
    <li style="left:276px;top:522px">Tantra</li>
    <li style="left:255px;top:592px">Intimrasur</li>
  </ul>

  <svg class="photo" style="left:729px;top:158px" width="240" height="240" viewBox="0 0 240 240">
    <defs>
      <radialGradient id="toneA" cx="50%" cy="45%" r="60%">
        <stop offset="0" stop-color="#c99272"/><stop offset="1" stop-color="#e9e3de"/>
      </radialGradient>
      <radialGradient id="toneB" cx="55%" cy="50%" r="60%">
        <stop offset="0" stop-color="#b9a8a8"/><stop offset="1" stop-color="#eeeeee"/>
      </radialGradient>
      <radialGradient id="toneC" cx="45%" cy="50%" r="60%">
        <stop offset="0" stop-color="#a8745a"/><stop offset="1" stop-color="#d8b5a0"/>
      </radialGradient>
    </defs>
    <circle cx="116" cy="120" r="117" fill="var(--lilac)"/>
    <circle cx="124" cy="118" r="110" fill="url(#toneA)" role="img" aria-label="Foto: entspannter Mann liegt auf der Massageliege"/>
  </svg>

  <svg class="photo" style="left:937px;top:320px" width="190" height="190" viewBox="0 0 190 190">
    <circle cx="92" cy="95" r="93" fill="var(--lilac)"/>
    <circle cx="99" cy="93" r="86" fill="url(#toneB)" role="img" aria-label="Foto: Hände massieren einen Männerrücken"/>
  </svg>

  <svg class="photo" style="left:1033px;top:496px" width="160" height="160" viewBox="0 0 160 160">
    <circle cx="77" cy="80" r="78" fill="var(--lilac)"/>
    <circle cx="83" cy="78" r="72" fill="url(#toneC)" role="img" aria-label="Foto: lächelnder Mann auf einem Handtuch"/>
  </svg>

  <div class="address">Studio 12 • Talweg 12 • München</div>
  <div class="website">velorin-point.com</div>
</div>
</body>
</html>
```